Bright Lantern Golf Club is a golf community dedicated to building productive relationships beginning with the unifying foundation of the great game.
Membership in the Bright Lantern Golf Club is simple, ask to join. The Membership Committee accepts a prospective member request upon confirmation of support for the club’s purpose.
The Bright Lantern Golf Club has only two rules:
1.) Create productive relationships building around an initial common thread
2.) When tempted to cut the last relationship thread, remember rule #1
Bright Lantern Golf Club members receive invitations to occasional club events but are also encouraged to create smaller events hosted by individual members. Members are not required to brand gatherings as official Bright Lantern Golf Club events. We believe when two or more of our members are together, the world gets better.
What are the dues? Members pay dues by sharing great stories, laughing often, encouraging each other to live well and by contributing to a meaningful cause outside of golf. If interested, please make a request for membership on the clubs Chatterbox page or send an email request to our Caddie Master at fairwayhost@pinemaillo.com.
If you join through our Chatterbox page, we encourage you to tag our page with testimonies about your common thread inspired experiences. For example, pictures of golf buddy trips and meaningful moments enjoying the great game with your family and friends.
We focus on what brings people together…
Target Market(s)
golfers who get the need to give back
Colors
Designer to choose colors to be used in the design.
Requirements
Must have
- clear messaging about the simple purpose vof the virtual club
- we can make up head quarter locations. like 19th holes around the world, global fairways, etc
- we do need a link to the club fairwayhost@pinemaillo.com
- logo very visible
Nice to have
- course pictures.... I can upload or send a few good ones
Should not have
- Pictures of virtual golf. I changed the summary

```html
<!DOCTYPE html>
<html lang="en">
<head>
<meta charset="utf-8">
<title>Bright Lantern Golf Club – Chatterbox Cover Preview</title>
<link rel="stylesheet" href="https://fonts.googleapis.com/css2?family=Montserrat:wght@100;300&family=Tinos:ital,wght@0,400;0,700;1,700&display=swap">
<style>
  :root {
    --page-bg: #0c0c0c;
    --accent: #f7941d;
    --accent-dark: #b8731c;
    --panel-white: #ffffff;
    --swoosh-grey: #d2d2d2;
    --forest: #3f5207;
    --ink: #111111;
    --light: #ffffff;
    --photo-dark: #2a2a2a;
    --photo-mid: #7d7d7d;
    --photo-light: #bdbdbd;
  }
  * { margin: 0; padding: 0; box-sizing: border-box; }
  html, body { width: 1200px; height: 1200px; overflow: hidden; background: var(--page-bg); }
  .canvas { position: relative; width: 1200px; height: 1200px; }

  .preview-title {
    position: absolute; top: 92px; left: 0; width: 1200px;
    text-align: center; color: var(--accent);
    font: 300 50px/1 "Montserrat", sans-serif; letter-spacing: 1px;
  }

  .cover {
    position: absolute; left: 120px; top: 186px; width: 960px; height: 355px;
    overflow: hidden; box-shadow: 0 14px 24px rgba(0,0,0,.6);
  }
  .cover-shapes { position: absolute; inset: 0; }

  .club-mark {
    position: absolute; left: 120px; top: 48px; width: 260px; height: 260px;
    border-radius: 50%; background: var(--accent-dark);
    display: flex; align-items: center; justify-content: center; text-align: center;
  }
  .club-mark-name {
    color: var(--light); font: 700 28px/1.15 "Tinos", serif;
    text-transform: uppercase; letter-spacing: 2px; width: 190px;
  }

  .cover-copy { position: absolute; left: 550px; color: var(--light); font-family: "Tinos", serif; }
  .intro { top: 14px; width: 400px; }
  .intro h1 { font-weight: 400; font-size: 26px; line-height: 1; color: var(--ink); white-space: nowrap; }
  .intro p { font-size: 17px; line-height: 21px; margin-top: 2px; }

  .membership { top: 131px; width: 400px; color: var(--accent); }
  .membership p { font-size: 13px; line-height: 16.5px; }
  .membership .name { color: var(--ink); }
  .membership h2 { font-weight: 400; font-size: 12px; color: var(--ink); margin-top: 7px; line-height: 15px; }
  .membership ol { list-style: none; font-size: 11px; line-height: 14.4px; }

  .dues { top: 262px; left: 552px; width: 400px; }
  .dues h2 { font-weight: 400; font-size: 24px; line-height: 1; color: var(--accent); }
  .dues p { font-size: 11px; line-height: 14.4px; font-weight: 700; margin-top: 1px; }
  .dues .email { color: var(--accent); font-style: italic; }

  .headline-updated {
    position: absolute; left: 0; top: 570px; width: 1200px; text-align: center;
    color: var(--accent); font: 100 98px/96px "Montserrat", sans-serif; letter-spacing: 2px;
  }
</style>
</head>
<body>
<div class="canvas">
  <h1 class="preview-title">CHATTERBOX COVER PREVIEW</h1>

  <section class="cover">
    <svg class="cover-shapes" width="960" height="355" viewBox="0 0 960 355">
      <defs>
        <linearGradient id="coast" x1="0" y1="0" x2="1" y2="1">
          <stop offset="0" stop-color="var(--photo-light)"/>
          <stop offset=".45" stop-color="var(--photo-mid)"/>
          <stop offset="1" stop-color="var(--photo-dark)"/>
        </linearGradient>
      </defs>
      <rect width="960" height="355" fill="url(#coast)" role="img" aria-label="Black and white photo of a coastal golf links above the sea"/>
      <path d="M480 0 Q580 178 480 355 L960 355 L960 0 Z" fill="var(--accent-dark)"/>
      <path d="M482 0 Q576 178 488 355 L960 355 L960 0 Z" fill="var(--panel-white)"/>
      <path d="M482 0 Q526 50 534 114 L960 114 L960 0 Z" fill="var(--accent)"/>
      <path d="M534 114 Q740 108 960 130 L960 114 Z" fill="var(--swoosh-grey)"/>
      <path d="M540 246 Q770 232 960 246 L960 355 L488 355 Q520 300 540 246 Z" fill="var(--forest)"/>
    </svg>

    <div class="club-mark"><span class="club-mark-name">Bright Lantern Golf Club</span></div>

    <div class="cover-copy intro">
      <h1>BRIGHT LANTERN GOLF CLUB</h1>
      <p>Is a golf community dedicated to building productive relationships beginning with the unifying foundation of the great game.</p>
    </div>

    <div class="cover-copy membership">
      <p>Membership in the <span class="name">Bright Lantern Golf Club</span> is simple, ask to join. The Membership Committee accepts a prospective member request upon confirmation of support for the club’s purpose.</p>
      <h2>THE BRIGHT LANTERN GOLF CLUB HAS ONLY TWO RULES:</h2>
      <ol>
        <li>1.) Create productive relationships building around an initial common thread</li>
        <li>2.) When tempted to cut the last relationship thread, remember rule #1</li>
      </ol>
    </div>

    <div class="cover-copy dues">
      <h2>WHAT ARE THE DUES?</h2>
      <p>Members pay dues by sharing great stories, laughing often, encouraging each other to live well and by contributing to a meaningful cause outside of golf.<br>
      If interested, please make a request for membership on the clubs Chatterbox page or send an email request to our Caddie Master at <a class="email">fairwayhost@pinemaillo.com.</a></p>
    </div>
  </section>

  <h2 class="headline-updated">UPDATED<br>DETAILS</h2>
</div>
</body>
</html>
```